Web Site Design for new Children's Book Series

We need a new web site design that complements a new children's book series that will be available next month. The main character is named 'Mippo Zelka Otter Cat Finch' and the story lines work through bullying issues for elementary age kids. This is a new design from scratch, but we have attached a collection of artwork from the new book series that the web site design should complement.

The scope of this project is only for the design / layout of the home page and one interior page for the web site.

Additional project details including the sitemap and example content are included in the attached document: 'Mippo Zelka Web Site.pdf'

We are open for questions and we look forward to seeing your creativity!
Updates

We have marked the project as guaranteed now!  We look forward to seeing your ideas and concepts!

Target Market(s)

Currently, there are two children’s books in the Mippo Zelka series aimed at elementary aged children. This collection is planned to grow over time. The goal of the web site is to provide information about the authors and the book series to elementary aged children (ages 3 to 12), their parents, and their school teachers and counselors.

Industry/Entity Type

Interior

Requirements
Must have
• The web site design should complement the attached artwork from the Mippo Zelka series. Overall, a full width design is desired that utilizes and open layout with lots of color.

The Mippo Zelka animal logo should be prominently placed. It is not necessary to retain the white background behind the logo.

The web site will be implemented as a responsive design using the Quill Scaffold framework and a standard 12 column grid.
Nice to have
• There are two themes in the books which should be incorporated into the web site design:

- Mippo Zelka uses the phrase “Way Cool” in describing various characters in the book and it is meant to build confidence and self esteem ... "you are way cool"

- An eagle feather is left behind as in “Zelka was here”. This eagle feature should be incorporated into the design in various locations.

```html
<!DOCTYPE html>
<html lang="en">
<head>
<meta charset="utf-8">
<title>Mippo Zelka Otter Cat Finch</title>
<link rel="stylesheet" href="https://fonts.googleapis.com/css2?family=Arimo:ital,wght@0,400;0,700;1,400;1,700&display=swap">
<style>
:root{
  --tan:#c9a07a;
  --tan-light:#d4ae8a;
  --teal:#4fbfb5;
  --teal-dark:#3aa99f;
  --ink:#1d1d1d;
  --charcoal:#3b3b3b;
  --grey:#d9d9d9;
  --white:#ffffff;
  --item:#d6b08c;
}
*{box-sizing:border-box;margin:0;padding:0}
html,body{width:823px;height:1200px;overflow:hidden;background:var(--white)}
body{position:relative;font-family:"Arimo",Arial,sans-serif;color:var(--ink)}
.abs{position:absolute}
a{color:inherit}

.hero{left:0;top:0;width:823px;height:331px;
  background:linear-gradient(180deg,var(--tan) 0%,var(--tan) 52%,#9db59f 72%,var(--teal) 100%)}
.util{top:18px;display:flex;gap:28px;font-size:8px;color:var(--white)}
.util span{display:flex;align-items:center;gap:5px}
.util svg{width:14px;height:14px}
.mainnav{left:129px;top:50px;width:561px;height:27px;
  background:linear-gradient(180deg,#f4f4f4,#c9c9c9);border-bottom:1px solid #999}
.mainnav a{position:absolute;top:7px;font-size:11px;text-decoration:none;color:var(--ink)}
.brand{left:335px;top:44px;width:158px;height:46px;background:var(--white);
  display:flex;align-items:center;justify-content:center;text-align:center;
  font-size:15px;font-weight:700;color:#c7462e;line-height:1.05;border:1px solid #bbb}
.intro{left:129px;top:83px;width:205px;font-size:7.5px;font-style:italic;font-weight:700;color:var(--white);line-height:1.3}
.news-title{left:138px;top:139px;font-size:13px;color:var(--ink)}
.news{left:129px;top:160px;width:294px;height:153px;background:var(--white);padding:8px 10px;font-size:9.4px;line-height:1.2}
.news h3{font-size:9.6px;font-style:italic;font-weight:700}
.news p{margin-bottom:3px}
.art{display:block}
.hero-art{left:427px;top:112px;width:281px;height:219px}
.cta-shop{left:557px;top:248px;width:124px;height:43px;background:var(--teal);border:1px solid #2d8f86;padding:5px 8px;font-size:9.5px;line-height:1.3}
.cta-author{left:696px;top:248px;width:127px;height:43px;background:var(--tan-light);padding:5px 8px;font-size:9.5px;line-height:1.3}

.signup{left:0;top:335px;width:129px;height:135px;background:var(--tan);padding:20px 8px 0 14px;font-size:9.2px;line-height:1.25}
.signup strong{font-size:11px;font-style:italic;display:block;margin-bottom:2px}
.newsletter{left:129px;top:377px;width:129px;height:93px;background:var(--teal);border:2px solid var(--charcoal)}
.newsletter div{background:var(--white);margin:8px;padding:4px 6px;font-size:10px;border:1px solid #999}
.newsletter i{display:block;margin:0 8px;height:5px;background:#cfe;border:1px solid #888}
.cast{left:0;top:470px;width:267px;height:137px;background:var(--charcoal);color:var(--white);padding:18px 0 0 18px;font-size:28px;font-weight:700;line-height:1.2}
.cast-art{left:184px;top:478px;width:83px;height:112px}
.cover-art{left:276px;top:350px;width:180px;height:211px}
.about{left:475px;top:359px;width:210px;font-size:10px;line-height:1.25}
.about b{font-size:13px;font-style:italic}
.lib-art{left:690px;top:331px;width:133px;height:151px}
.libraries{left:690px;top:482px;width:133px;height:92px;background:var(--teal);padding:8px 10px;font-size:10px;line-height:1.25}
.libraries b{font-style:italic;font-size:11.5px}

.band{left:0;top:607px;width:823px;height:77px;background:linear-gradient(180deg,#f2f2f2,#c4c4c4)}
.waycool{left:147px;top:625px;font-size:21px;font-weight:700}
.waycool-sub{left:294px;top:626px;width:150px;font-size:9.5px;color:#444;line-height:1.25}

.side{left:129px;width:147px}
.share{top:684px;height:48px;border:2px solid var(--charcoal);padding:5px 8px;font-size:13px;line-height:1.2}
.portal-head{height:18px;padding:4px 6px;font-size:8.5px;color:var(--white)}
.head-teal{background:var(--teal)}
.head-dark{background:var(--charcoal)}
.portal-list{list-style:none}
.portal-list li{height:17.5px;padding:4px 6px;font-size:8.3px;background:var(--item);border-bottom:1px solid #e7cdb3}
.stories{left:285px;top:688px;width:405px;font-size:6.8px;line-height:1.28}
.stories p{margin-bottom:8px}

.foot{left:0;top:1113px;width:823px;height:87px;background:var(--teal)}
.foot-col{top:1148px;font-size:11px;line-height:1.45}
</style>
</head>
<body>

<section class="abs hero"></section>

<nav class="abs util" style="left:129px">
  <span><svg viewBox="0 0 14 14"><circle cx="7" cy="7" r="6" fill="#fff"/></svg>Publisher</span>
  <span><svg viewBox="0 0 14 14"><circle cx="7" cy="7" r="6" fill="#fff"/></svg>Author</span>
</nav>
<nav class="abs util" style="left:553px">
  <span><svg viewBox="0 0 14 14"><circle cx="7" cy="7" r="6" fill="#fff"/></svg>Shop</span>
  <span><svg viewBox="0 0 14 14"><circle cx="7" cy="7" r="6" fill="#fff"/></svg>Newsletter</span>
</nav>

<nav class="abs mainnav">
  <a style="left:20px">Story</a>
  <a style="left:102px">Characters</a>
  <a style="left:412px">Author</a>
  <a style="left:484px">Shop Now</a>
</nav>
<div class="abs brand">Mippo Zelka<br>Otter Cat Finch</div>

<p class="abs intro">Introducing, Mippo Zelka! Follow the thrilling adventures of Mippo Zelka Otter Cat Finch</p>

<h2 class="abs news-title">Latest News</h2>
<article class="abs news">
  <h3>A mom of three in Nebraska shares how Mippo Zelka brought her family closer</h3>
  <p>It was a bright sunny Monday morning, the older two were off to school and I was finishing up some emails...</p>
  <h3>Schoolteacher, Wren, asks her students this very important question</h3>
  <p>Wren has been teaching for over twenty years, but...</p>
</article>

<svg class="abs art hero-art" role="img" aria-label="Illustration of the two main characters" viewBox="0 0 281 219" preserveAspectRatio="none">
  <defs><linearGradient id="heroG" x1="0" y1="0" x2="0" y2="1"><stop offset="0" stop-color="#a8744f"/><stop offset="1" stop-color="#8a5a3a"/></linearGradient></defs>
  <rect width="281" height="219" fill="url(#heroG)" opacity=".55"/>
</svg>

<div class="abs cta-shop">In Stores Now!<br>Visit the shop here.</div>
<div class="abs cta-author">Learn more about the author.</div>

<div class="abs signup"><strong>Don't miss a thing!</strong>Sign-up for the Mippo Zelka Email Newsletter. We just need your email address. Sign-up here.</div>
<div class="abs newsletter"><div>MZ Newsletter</div><i></i></div>

<div class="abs cast">Meet the<br>cast &amp;<br>characters</div>
<svg class="abs art cast-art" role="img" aria-label="Illustration of the finch character" viewBox="0 0 83 112" preserveAspectRatio="none">
  <rect width="83" height="112" fill="#6b6158"/>
</svg>

<svg class="abs art cover-art" role="img" aria-label="Book cover of the first Mippo Zelka story" viewBox="0 0 180 211" preserveAspectRatio="none">
  <defs><linearGradient id="coverG" x1="0" y1="0" x2="1" y2="1"><stop offset="0" stop-color="#7fcfc6"/><stop offset="1" stop-color="#b98a5e"/></linearGradient></defs>
  <rect x="20" y="8" width="140" height="190" fill="url(#coverG)"/>
</svg>

<p class="abs about"><b>About the book</b> Mippo, the otter cat and Zelka, the finch, lived along the Pamlico River in Bath, North Carolina. While playing one day, they became an unusual character named Mippo Zelka Otter Cat Finch. Mippo and Zelka travel throughout the book adjusting to their new body and learning how to use their "super powers" for good. To learn more about the book, <a href="#">click here</a> to visit the about page.</p>

<svg class="abs art lib-art" role="img" aria-label="Photo of a young girl reading a book in a library" viewBox="0 0 133 151" preserveAspectRatio="none">
  <defs><linearGradient id="libG" x1="0" y1="0" x2="0" y2="1"><stop offset="0" stop-color="#e9d6c4"/><stop offset="1" stop-color="#c98aa8"/></linearGradient></defs>
  <rect width="133" height="151" fill="url(#libG)"/>
</svg>
<div class="abs libraries"><b>Libraries</b> Are you a librarian? Find out how to get a copy in your location. <a href="#">Here.</a></div>

<section class="abs band"></section>
<h2 class="abs waycool">"Way cool"</h2>
<p class="abs waycool-sub">Ways Mippo Zelka is helping children learn all across the country</p>

<div class="abs side share">Share your story here</div>

<div class="abs side" style="top:740px">
  <div class="portal-head head-teal">Teacher Portal</div>
  <ul class="portal-list">
    <li>Login</li><li>Register</li><li>Teacher's Copy</li><li>Curriculum guide</li><li>Educator's discount</li><li>eBook version</li>
  </ul>
</div>
<div class="abs side" style="top:880px">
  <div class="portal-head head-dark">Parent Portal</div>
  <ul class="portal-list">
    <li>Morals and values</li><li>Reading age</li><li>Important questions</li>
  </ul>
</div>
<div class="abs side" style="top:976px">
  <div class="portal-head head-teal">Library Portal</div>
  <ul class="portal-list">
    <li>Bulk rates</li><li>Shipping</li><li>eBook version</li><li>Book signing and readings</li>
  </ul>
</div>

<div class="abs stories">
  <p>"We were surprised when Teodor came through the door yelling, 'I'm finished!' Teodor struggles with reading and we thought it was because he couldn't understand phonics. We tried everything. His teacher, Ilse at Fernhollow Books in San Francisco told us to find a book that he would enjoy. We searched and searched until we came upon 'Mippo Zelka'. Teodor read through the book he first week with it. After that, he read it 5 more times. We started a local book club with other kids his age and developed a small game that they play together. The game is now available in my blog (www.lanternmom.example) and I would love to share it with any of your readers. Thank you, Pell, for bringing this book into our lives. Our Teodor will not look back in his reading skills" - Marisol, San Francisco, California</p>
  <p>"We were surprised when Teodor came through the door yelling, 'I'm finished!' Teodor struggles with reading and we thought it was because he couldn't understand phonics. We tried everything. His teacher, Ilse at Fernhollow Books in San Francisco told us to find a book that he would enjoy. We searched and searched until we came upon your book. Thank you, thank you" - Marisol, San Francisco, Nebraska</p>
  <p>"We were surprised when Teodor came through the door yelling, 'I'm finished!' Teodor struggles with reading and we thought it was because he couldn't understand phonics. We tried everything. His teacher, Ilse at Fernhollow Books in San Francisco told us to find a book that he would enjoy. We searched and searched until we came upon 'Mippo Zelka.'" - Dov, Newark</p>
  <p>"We were surprised when Teodor came through the door yelling, 'I'm finished!' Teodor struggles with reading and we thought it was because he couldn't understand phonics. We tried everything. His teacher, Ilse at Fernhollow Books in San Francisco told us to find a book that he would enjoy. We searched and searched until we came upon 'Mippo Zelka'.And that is only the beginning of the story" - Odette, Long Island</p>
  <p>"A triumphant recovery for a lack of creativity in children's books" - The Daily Lantern. Montana</p>
</div>

<footer class="abs foot"></footer>
<nav class="abs util" style="left:147px;top:1127px">
  <span><svg viewBox="0 0 14 14"><circle cx="7" cy="7" r="6" fill="#fff"/></svg>Publisher</span>
  <span><svg viewBox="0 0 14 14"><circle cx="7" cy="7" r="6" fill="#fff"/></svg>Author</span>
</nav>
<nav class="abs util" style="left:540px;top:1127px">
  <span><svg viewBox="0 0 14 14"><circle cx="7" cy="7" r="6" fill="#fff"/></svg>Shop</span>
  <span><svg viewBox="0 0 14 14"><circle cx="7" cy="7" r="6" fill="#fff"/></svg>Newsletter</span>
</nav>
<div class="abs foot-col" style="left:158px">Author<br>Story</div>
<div class="abs foot-col" style="left:230px">Shop Now<br>Characters</div>
<div class="abs foot-col" style="left:543px">This<br>Author</div>
<div class="abs foot-col" style="left:615px">Story<br>Shop Now</div>

</body>
</html>
```